Shopping centre customer engagement software website

We need a multi page site with :

*What we do.
*How it works.
*Benefits
* Case study
* Testimonial
* Business login (we provide link to business portal)
* Consumer login (we provide link to consumer site)
* Book a demo
* Contact us

We want it to be clean and crisp and very self explanatory with little clutter. We are thinking white but are open to what ever looks the best.
Updates

Wordpress is preferred

Need extra days to review

Target Market(s)

Shopping centre managers and retail property companies

Coding

Coded - Design and coding required

Number of Pages Required

5+ page

Font styles to use
Sans Serif

Colors
ffffff

Requirements
Must have
• As listed above and must be responsive! Checkout our existing site for the text to be included (will be edited but it’ll give you an idea) www.vantrizo.com

```html
<!DOCTYPE html>
<html lang="en">
<head>
<meta charset="utf-8">
<title>Vantrizo — Shopping Centre Engagement</title>
<link href="https://fonts.googleapis.com/css2?family=Raleway:wght@200;300;500;600;700&family=Roboto:ital,wght@0,400;0,500;1,400&display=swap" rel="stylesheet">
<style>
:root{
  --teal:#5bb8c9;
  --teal-dark:#3fa3b6;
  --ink:#2e2e2e;
  --text:#6f6f6f;
  --muted:#9a9a9a;
  --panel:#f1f1f1;
  --panel-2:#e9e9e9;
  --white:#ffffff;
  --night:#2c3138;
}
*{box-sizing:border-box;margin:0;padding:0}
html,body{width:1200px;height:3614px;overflow:hidden;background:var(--white)}
body{position:relative;font-family:'Roboto',sans-serif;color:var(--text)}
.abs{position:absolute}
h2{font-family:'Raleway',sans-serif;font-weight:600;color:var(--ink);font-size:31px;letter-spacing:.5px}
p{font-size:14px;line-height:23px}
.btn{position:absolute;display:flex;align-items:center;justify-content:center;border-radius:30px;font-family:'Raleway',sans-serif;font-weight:600;font-size:13px;text-transform:uppercase;background:var(--teal);color:var(--white)}
/* header */
.site-header{top:0;left:0;width:1200px;height:108px;background:var(--white)}
.brand{left:100px;top:40px;font-family:'Raleway',sans-serif;font-weight:600;font-size:20px;color:var(--ink);letter-spacing:1px}
.nav a{position:absolute;top:44px;font-family:'Raleway',sans-serif;font-weight:700;font-size:13px;color:var(--ink);text-decoration:none}
.btn-demo{left:800px;top:34px;width:140px;height:42px}
.btn-business{left:954px;top:34px;width:150px;height:42px;background:var(--white);color:var(--teal);border:2px solid var(--teal)}
/* hero */
.hero{top:108px;left:0;width:1200px;height:722px;overflow:hidden}
.hero-photo{position:absolute;inset:0;background:linear-gradient(180deg,#8d949a 0%,#b8bec3 45%,#6d747b 100%)}
.hero-device{left:120px;top:72px;width:195px;height:560px;border-radius:22px;background:linear-gradient(180deg,#f2f2f2,#c9ccd0);transform:rotate(-4deg)}
.hero-title{right:96px;top:160px;font-family:'Raleway',sans-serif;font-weight:200;font-size:96px;letter-spacing:10px;color:var(--white)}
.hero-tag{right:96px;top:296px;width:700px;text-align:right;font-size:24px;line-height:41px;color:var(--white);white-space:nowrap}
.btn-vip{left:776px;top:393px;width:128px;height:41px}
.btn-video{left:920px;top:393px;width:181px;height:41px;background:rgba(0,0,0,.15);border:2px solid var(--white);justify-content:flex-start;padding-left:18px}
.play{position:absolute;right:8px;top:7px;width:24px;height:24px;border-radius:50%;background:var(--white)}
.hero-wave{left:0;bottom:0}
/* welcome */
.monitor{left:101px;top:855px}
.welcome-title{left:602px;top:868px}
.welcome-text{left:602px;top:913px;width:500px}
.btn-welcome{left:602px;top:1090px;width:148px;height:43px}
/* what we do */
.what-panel{top:1240px;left:0;width:600px;height:495px;background:var(--panel)}
.what-title{left:101px;top:1302px}
.what-text{left:101px;top:1376px;width:460px}
.btn-what{left:96px;top:1622px;width:152px;height:46px}
.what-photo{top:1240px;left:600px;width:600px;height:495px;background:linear-gradient(135deg,#6b5a46,#c9a979 55%,#3f4a55)}
/* benefits */
.benefits-photo{top:1735px;left:0;width:600px;height:482px;background:linear-gradient(135deg,#e9e3d8,#b9a892 60%,#8a8f95)}
.benefits-panel{top:1735px;left:600px;width:600px;height:482px;background:var(--panel-2)}
.benefits-title{left:663px;top:1800px}
.benefits-text{left:663px;top:1862px;width:480px;font-size:12px;line-height:20px;color:var(--muted)}
.benefit{position:absolute;top:1935px;width:170px;text-align:center}
.benefit-ring{width:106px;height:106px;margin:0 auto;border-radius:50%;border:5px solid var(--teal);display:flex;align-items:center;justify-content:center;background:var(--white)}
.benefit-label{margin-top:26px;font-size:13px;line-height:19px;color:var(--ink)}
.btn-benefits{left:823px;top:2124px;width:90px;height:30px;font-size:11px}
.caret{position:absolute;top:1975px;font-size:30px;color:#888;font-family:'Roboto',sans-serif}
/* how it works */
.how-title{left:0;top:2315px;width:1200px;text-align:center}
.how-text{left:360px;top:2372px;width:480px;text-align:center;font-size:13px;line-height:21px}
.step{position:absolute;top:2470px;width:200px;text-align:center}
.step-ring{position:relative;width:140px;height:140px;margin:0 auto;border-radius:50%;background:var(--white);box-shadow:0 0 0 1px #ececec,0 2px 10px rgba(0,0,0,.06);display:flex;align-items:center;justify-content:center}
.step-num{position:absolute;right:-2px;bottom:8px;width:28px;height:28px;border-radius:50%;background:var(--teal);color:var(--white);font-size:13px;font-weight:500;display:flex;align-items:center;justify-content:center}
.step-label{margin-top:24px;font-family:'Raleway',sans-serif;font-weight:700;font-size:16px;color:var(--ink)}
.flow{left:0;top:2470px}
/* case study */
.case{top:2742px;left:0;width:1200px;height:555px;background:linear-gradient(135deg,#3a4047,#6d737a 50%,#2e3339)}
.case-title{left:0;top:2813px;width:1200px;text-align:center;color:var(--white)}
.case-card{left:101px;top:2909px;width:407px;height:320px;background:var(--white)}
.case-photo{position:absolute;left:0;top:0;width:407px;height:272px;background:linear-gradient(135deg,#7f8a94,#cfd5da 50%,#5d666f)}
.case-stat{position:absolute;left:24px;bottom:12px;font-family:'Raleway',sans-serif;font-weight:700;font-size:14px;color:var(--ink);display:flex;align-items:center;gap:22px}
.case-stat span{font-family:'Roboto',sans-serif;font-weight:400;color:var(--text);display:flex;align-items:center;gap:8px}
.quote{left:602px;top:2912px;width:515px;font-style:italic;font-size:13.5px;line-height:23px;color:var(--white)}
.author{left:947px;top:3106px;font-family:'Raleway',sans-serif;font-weight:700;font-size:15px;color:var(--white)}
.city{left:947px;top:3138px;font-size:13px;color:var(--white)}
.slide-arrow{top:2956px;font-size:40px;color:var(--white);font-weight:300}
/* contact */
.contact{top:3297px;left:0;width:1200px;height:241px;background:#f4f4f4}
.contact-title{left:101px;top:3358px;font-size:19px;font-weight:700}
.cinfo{position:absolute;font-size:12px;line-height:19px;color:var(--text);padding-left:26px}
.cinfo svg{position:absolute;left:0;top:3px}
.social{position:absolute;top:3420px;width:38px;height:38px;border-radius:50%;border:1px solid #cfcfcf}
/* footer */
.site-footer{top:3538px;left:0;width:1200px;height:76px;border-top:1px solid #e2e2e2;display:flex;align-items:center;justify-content:center;font-size:12px;color:var(--text)}
</style>
</head>
<body>

<header class="abs site-header">
  <div class="abs brand">VANTRIZO</div>
  <nav class="nav">
    <a style="left:282px">WHAT WE DO</a>
    <a style="left:417px">BENEFITS</a>
    <a style="left:528px">HOW IT WORKS</a>
    <a style="left:675px">CASE STUDY</a>
  </nav>
  <a class="btn btn-demo">Request Demo</a>
  <a class="btn btn-business">Business Login</a>
</header>

<section class="abs hero">
  <div class="hero-photo" role="img" aria-label="Photo of a bright multi-level shopping centre interior"></div>
  <div class="abs hero-device" role="img" aria-label="Photo of a smart loyalty card device"></div>
  <div class="abs hero-title">VANTRIZO</div>
  <div class="abs hero-tag">Vantrizo exceeds all expectations forShopping Centre<br>Managers Shoppers, Tenants and Landlords</div>
  <a class="btn btn-vip">VIP Login</a>
  <a class="btn btn-video">Watch Video<span class="play"></span></a>
  <svg class="abs hero-wave" width="1200" height="260" viewBox="0 0 1200 260">
    <path d="M0 150 C 300 270, 700 250, 1200 40 L1200 260 L0 260 Z" fill="#ffffff"/>
  </svg>
</section>

<section class="welcome">
  <svg class="abs monitor" width="436" height="280" viewBox="0 0 436 280" role="img" aria-label="Monitor showing the dashboard">
    <rect x="0" y="0" width="436" height="248" rx="6" fill="#111"/>
    <rect x="10" y="10" width="416" height="226" fill="#e9edf0"/>
    <rect x="10" y="10" width="60" height="226" fill="#2b3440"/>
    <rect x="80" y="22" width="104" height="42" fill="#5bb8c9"/>
    <rect x="192" y="22" width="104" height="42" fill="#47a7e0"/>
    <rect x="304" y="22" width="110" height="42" fill="#f1666a"/>
    <rect x="80" y="76" width="334" height="150" fill="#ffffff"/>
    <path d="M88 218 C150 110, 190 120, 240 200 S 340 90, 406 190" fill="none" stroke="#e8c37a" stroke-width="2"/>
    <path d="M88 218 C160 170, 220 160, 280 205 S 360 180, 406 212" fill="none" stroke="#8fd3c6" stroke-width="2"/>
    <path d="M178 248 L258 248 L270 270 L166 270 Z" fill="#111"/>
    <rect x="120" y="270" width="196" height="8" rx="3" fill="#111"/>
  </svg>
  <h2 class="abs welcome-title">WELCOME TO VANTRIZO</h2>
  <p class="abs welcome-text">Lorem ipsum dolor sit amet, consectetur adipiscing elit, sed do eiusmod tempor incididunt ut labore et dolore magna aliqua. Ut enim ad minim veniam, quis nostrud exercitation ullamco laboris nisi ut aliquip ex ea commodo consequat. Duis aute dolor in reprehenderit in voluptate velit esse cillum dolore fugiat nulla pariatur, perspiciatis unde omnis iste natus error sit voluptatem accusantium doloremque laudantium, totam rem aperiam.</p>
  <a class="btn btn-welcome">Read More &gt;&gt;</a>
</section>

<section class="what">
  <div class="abs what-panel"></div>
  <h2 class="abs what-title">WHAT WE DO</h2>
  <div class="abs what-text">
    <p style="font-size:13px;line-height:22px">Vantrizo provides shopping centre managers with an easy to use platform which enables them to delight their shoppers, impress their tenants, provide detailed data to their landlords and all accessible to them at the click of button.</p>
    <p style="font-size:13px;line-height:22px;margin-top:22px">Vantrizo gives shopping centres real time tracking through smart ID's of individual customer journeys through their physical stores, enabling highly targeted, relevant and timely promotional and rewarding capabilities. Furthermore, through deep analytical data processing of the customer journey, centre managers will be able to more accurately and reliably predict shopping behaviours.</p>
  </div>
  <a class="btn btn-what">Read More &gt;&gt;</a>
  <div class="abs what-photo" role="img" aria-label="Photo of developers working at computer screens"></div>
</section>

<section class="benefits">
  <div class="abs benefits-photo" role="img" aria-label="Photo of a shopper on a sofa paying online with a laptop and card"></div>
  <div class="abs benefits-panel"></div>
  <h2 class="abs benefits-title">BENEFITS</h2>
  <p class="abs benefits-text">At vero eos et accusamus et iusto odio dignissimos ducimus qui blanditiis praesentium voluptatum deleniti atque corrupti quos dolores quas molestias.</p>
  <span class="caret" style="left:614px">&#8249;</span>
  <span class="caret" style="left:1100px">&#8250;</span>
  <div class="benefit" style="left:628px">
    <div class="benefit-ring"><svg width="44" height="44" viewBox="0 0 44 44"><rect x="6" y="8" width="32" height="24" rx="2" fill="#3f6fa8"/><circle cx="31" cy="30" r="8" fill="#f39c34"/></svg></div>
    <div class="benefit-label">Easy to install,<br>no wiring required</div>
  </div>
  <div class="benefit" style="left:780px">
    <div class="benefit-ring"><svg width="44" height="44" viewBox="0 0 44 44"><rect x="8" y="6" width="28" height="32" rx="3" fill="#e2513f"/><rect x="15" y="14" width="14" height="14" fill="#fff"/></svg></div>
    <div class="benefit-label">Easy to use dashboard<br>with one click reporting</div>
  </div>
  <div class="benefit" style="left:937px">
    <div class="benefit-ring"><svg width="44" height="44" viewBox="0 0 44 44"><path d="M10 28 a8 8 0 0 1 2-15 a11 11 0 0 1 21 3 a6 6 0 0 1 0 12 Z" fill="#7fb9d8"/><rect x="18" y="26" width="8" height="10" fill="#5a8fb0"/></svg></div>
    <div class="benefit-label">Have the data to back up<br>any decision's you make.</div>
  </div>
  <a class="btn btn-benefits">Read More</a>
</section>

<section class="how">
  <h2 class="abs how-title">HOW IT WORKS</h2>
  <p class="abs how-text">Sed quia non numquam eius modi tempora incidunt ut labore et dolore magnam aliquam quaerat voluptatem</p>
  <svg class="abs flow" width="1200" height="140" viewBox="0 0 1200 140">
    <g fill="none" stroke="#5bb8c9" stroke-width="6" stroke-linecap="round">
      <path d="M245 82 Q 275 66 305 72"/><path d="M457 82 Q 487 66 517 72"/>
      <path d="M669 82 Q 699 66 729 72"/><path d="M881 82 Q 911 66 941 72"/>
    </g>
    <g fill="#5bb8c9">
      <path d="M300 62 L318 73 L300 82 Z"/><path d="M512 62 L530 73 L512 82 Z"/>
      <path d="M724 62 L742 73 L724 82 Z"/><path d="M936 62 L954 73 L936 82 Z"/>
    </g>
  </svg>
  <div class="step" style="left:64px"><div class="step-ring"><svg width="56" height="46" viewBox="0 0 56 46"><rect x="4" y="4" width="40" height="26" rx="3" fill="#f2b23a"/><rect x="12" y="14" width="40" height="26" rx="3" fill="#4a8fc9"/></svg><span class="step-num">1</span></div><div class="step-label">Allocate Cards</div></div>
  <div class="step" style="left:286px"><div class="step-ring"><svg width="56" height="46" viewBox="0 0 56 46"><path d="M6 18 L30 6 L30 40 L6 28 Z" fill="#2d4c6e"/><rect x="2" y="18" width="8" height="10" fill="#e2513f"/><circle cx="44" cy="12" r="5" fill="#4a8fc9"/><circle cx="46" cy="32" r="5" fill="#e2513f"/></svg><span class="step-num">2</span></div><div class="step-label">Direct Marketing</div></div>
  <div class="step" style="left:498px"><div class="step-ring"><svg width="50" height="50" viewBox="0 0 50 50"><circle cx="25" cy="20" r="15" fill="#2d4c6e"/><circle cx="25" cy="20" r="7" fill="#f2b23a"/><path d="M16 32 L12 46 L20 42 L25 48 L30 42 L38 46 L34 32 Z" fill="#e2513f"/></svg><span class="step-num">3</span></div><div class="step-label">Rewarding Loyalty</div></div>
  <div class="step" style="left:719px"><div class="step-ring"><svg width="56" height="46" viewBox="0 0 56 46"><rect x="6" y="10" width="44" height="32" rx="2" fill="#f2b23a"/><rect x="12" y="4" width="32" height="14" fill="#4a8fc9"/><rect x="6" y="20" width="44" height="22" fill="#e9a12e"/></svg><span class="step-num">4</span></div><div class="step-label">Collect Data</div></div>
  <div class="step" style="left:931px"><div class="step-ring"><svg width="50" height="50" viewBox="0 0 50 50"><circle cx="22" cy="22" r="14" fill="none" stroke="#2d4c6e" stroke-width="5"/><rect x="15" y="22" width="4" height="8" fill="#4a8fc9"/><rect x="21" y="17" width="4" height="13" fill="#e2513f"/><rect x="27" y="20" width="4" height="10" fill="#f2b23a"/><path d="M32 32 L44 44" stroke="#2d4c6e" stroke-width="6" stroke-linecap="round"/></svg><span class="step-num">5</span></div><div class="step-label">Data Analysis</div></div>
</section>

<section class="abs case" role="img" aria-label="Blurred photo of shoppers walking through a mall"></section>
<h2 class="abs case-title">CASE STUDY &amp; TESTIMONIAL</h2>
<span class="abs slide-arrow" style="left:44px">&#8249;</span>
<span class="abs slide-arrow" style="left:1134px">&#8250;</span>
<div class="abs case-card">
  <div class="case-photo" role="img" aria-label="Photo of a hand holding a phone showing a new message"></div>
  <div class="case-stat">MESSAGES SENT <span><svg width="18" height="14" viewBox="0 0 18 14"><path d="M2 1 H16 V10 H7 L3 13 V10 H2 Z" fill="#5bb8c9"/></svg>10500</span></div>
</div>
<p class="abs quote">" Sed ut perspiciatis unde omnis iste natus error sit voluptatem accusantium doloremque laudantium, totam rem aperiam, eaque ipsa quae ab illo inventore veritatis et quasi architecto beatae vitae dicta sunt explicabo. Nemo enim ipsam voluptatem quia voluptas sit aspernatur aut odit aut fugit, sed quia consequuntur magni dolores eos qui ratione voluptatem sequi nesciunt. Neque porro quisquam est, qui dolorem ipsum quia dolor sit amet, consectetur, adipisci velit, sed quia non numquam eius modi tempora incidunt ut labore et dolore. "</p>
<div class="abs author">- Author Name</div>
<div class="abs city">City Location</div>

<section class="abs contact"></section>
<h2 class="abs contact-title">CONTACT US</h2>
<div class="cinfo" style="left:101px;top:3412px"><svg width="12" height="12" viewBox="0 0 12 12"><path d="M11 1 L1 5 L6 6 L7 11 Z" fill="#777"/></svg>Unit 7b, Harbour Road<br>Carrowmore, CM12 4QT</div>
<div class="cinfo" style="left:101px;top:3470px"><svg width="12" height="12" viewBox="0 0 12 12"><rect x="0" y="2" width="12" height="8" fill="#777"/><path d="M0 2 L6 7 L12 2" fill="none" stroke="#f4f4f4"/></svg>dara@vantrizo.com</div>
<div class="cinfo" style="left:277px;top:3412px"><svg width="12" height="12" viewBox="0 0 12 12"><path d="M11 1 L1 5 L6 6 L7 11 Z" fill="#777"/></svg>Foundry, 3rd Floor 41 Lower Quay<br>Street , Ashby, AB3 7LN</div>
<div class="cinfo" style="left:277px;top:3470px"><svg width="12" height="12" viewBox="0 0 12 12"><rect x="0" y="2" width="12" height="8" fill="#777"/><path d="M0 2 L6 7 L12 2" fill="none" stroke="#f4f4f4"/></svg>milo@vantrizo.com</div>
<div class="cinfo" style="left:525px;top:3412px"><svg width="12" height="12" viewBox="0 0 12 12"><path d="M11 1 L1 5 L6 6 L7 11 Z" fill="#777"/></svg>4th Floor, Keystone House<br>Mercer Street, Dunmore</div>
<div class="cinfo" style="left:525px;top:3470px"><svg width="12" height="12" viewBox="0 0 12 12"><rect x="0" y="2" width="12" height="8" fill="#777"/><path d="M0 2 L6 7 L12 2" fill="none" stroke="#f4f4f4"/></svg>ross@vantrizo.com</div>
<div class="cinfo" style="left:740px;top:3412px"><svg width="12" height="12" viewBox="0 0 12 12"><path d="M2 1 L5 1 L6 4 L4 5 Q5 8 7 8 L8 6 L11 7 L11 10 Q4 12 1 3 Z" fill="#777"/></svg>Phone | 0281 447 3952</div>
<div class="cinfo" style="left:740px;top:3442px"><svg width="12" height="12" viewBox="0 0 12 12"><rect x="0" y="2" width="12" height="8" fill="#777"/><path d="M0 2 L6 7 L12 2" fill="none" stroke="#f4f4f4"/></svg>Email | contact@vantrizo.com</div>
<span class="social" style="left:962px" aria-label="Social link"></span>
<span class="social" style="left:1010px" aria-label="Social link"></span>
<span class="social" style="left:1063px" aria-label="Social link"></span>

<footer class="abs site-footer">Copyrights © Vantrizo 2018. All Rights Reserved.</footer>

</body>
</html>
```